Webdesign für Maklerbüro
Zielgruppe
Wir sind ein Maklerbüro aus Nürnberg, das sich auf den Verkauf von Eigentumswohnungen und Häuser spezialisiert hat. Mit der neuen Seite möchten wir vor allem Eigentümer ansprechen und über unsere Arbeitsweise informieren. Der Hauptzweck ist damit die Akquise von neuen Objekten, für die Vermittlung. Die Zielgruppe sind vornehmlich Immobilienbesitzer im Alter 40+ und im gehobenen Preissegment.
Aufgabenstellung
Beim Design bitte an den Vorgaben des Logo (Datei beigefügt) orientieren. Bilder und Texte können durch 'Platzhalter' ersetzt werden.
Grundsätzlich stellt es für uns kein Problem dar, sich an Template-Vorlagen zu orientieren. Wir stellen uns eine Seite mit Pfiff und Ideenreichtum – einfach weg vom Standard – vor. Wir verkaufen Immobilien, aber vom verstaubten Krawattenträger sind wir weit entfernt. Wir sind ein junges Unternehmen, das neue Marketingwege beschreitet. Unsere Webseite muss das ausdrücken. Kein Standard, und damit auch keine Standard-Webseite. Designs, die uns gut gefallen (und in die Richtung es auch gehen kann) haben wir beigefügt.

```html
<!DOCTYPE html>
<html lang="de">
<head>
<meta charset="utf-8">
<title>Wohnwerk Franken – Immobilienmakler Nürnberg</title>
<link rel="stylesheet" href="https://fonts.googleapis.com/css2?family=Montserrat:wght@600;700;800&family=Open+Sans:ital,wght@0,300;0,400;0,600;1,300&display=swap">
<style>
:root{
  --navy:#1b2340;
  --ink:#1c1f2b;
  --blue:#1a8fd6;
  --btn-blue:#1a9ad8;
  --band:#2c3648;
  --grey-bg:#f2f2f2;
  --text:#444;
  --white:#fff;
}
*{box-sizing:border-box;margin:0;padding:0}
html,body{width:1200px;height:3722px;overflow:hidden}
body{position:relative;background:var(--white);font-family:"Open Sans",sans-serif;color:var(--text)}
.abs{position:absolute}
.heading{font-family:"Montserrat",sans-serif;font-weight:800}
.brand{font-family:"Montserrat",sans-serif;font-weight:800;letter-spacing:.5px;display:flex;align-items:center;gap:10px}
.brand .dot{width:14px;height:14px;background:var(--blue)}
/* header */
.site-logo{left:126px;top:44px;font-size:22px;color:var(--navy)}
.main-nav{right:126px;top:58px;display:flex;gap:22px;font-family:"Montserrat",sans-serif;font-weight:700;font-size:11.5px;color:var(--ink)}
.hero-title{left:126px;top:222px;font-size:35px;line-height:47px;color:var(--ink)}
/* audience tiles */
.tile{top:426px;width:300px;height:228px}
.tile-caption{top:670px;width:300px;text-align:right;font-family:"Montserrat",sans-serif;font-weight:700;font-size:12.5px;color:var(--ink)}
/* intro */
.intro-title{left:448px;top:854px;font-size:26px;color:var(--blue)}
.intro-text{left:448px;top:910px;width:628px;font-size:11.8px;line-height:18.8px}
.intro-text p+p{margin-top:4px}
.cta-label{left:448px;top:1190px;font-family:"Montserrat",sans-serif;font-weight:700;font-size:12.5px;color:var(--ink)}
.btn{display:flex;align-items:center;justify-content:center;font-family:"Montserrat",sans-serif;font-weight:700;font-size:12.5px;color:var(--white);background:var(--navy)}
.cta-btn{left:725px;top:1176px;width:204px;height:40px}
/* services band */
.band{left:0;top:1324px;width:1200px;height:457px;background:linear-gradient(180deg,#3a4558 0%,#2c3648 55%,#262f40 100%)}
.band-kicker{left:126px;top:1404px;font-size:12.5px;color:var(--white)}
.band-title{left:126px;top:1428px;font-size:26px;color:var(--blue)}
.band-link{left:126px;top:1467px;font-size:12.5px;color:var(--white);text-decoration:underline}
.service-icon{top:1536px;width:72px;height:72px}
.service{top:1538px;width:206px;color:var(--white)}
.service h3{font-family:"Montserrat",sans-serif;font-weight:700;font-size:13px;margin-bottom:8px}
.service p{font-size:11.8px;line-height:18.4px}
/* references */
.ref-title{left:126px;top:1866px;font-size:26px;color:var(--blue)}
.ref-text{left:126px;top:1911px;width:640px;font-size:12px;line-height:18.8px;color:var(--ink)}
.card{top:1980px;width:461px;height:336px}
.card-frame{position:absolute;left:21px;top:21px;right:21px;bottom:21px;border:2px solid var(--white)}
.card h4{position:absolute;left:40px;top:202px;font-family:"Montserrat",sans-serif;font-weight:700;font-size:17px;color:var(--white)}
.card .sub{position:absolute;left:40px;top:226px;font-size:12px;color:#e4e8ee}
.card .btn{position:absolute;left:40px;top:258px;width:166px;height:38px}
/* testimonials */
.quotes-bg{left:0;top:2412px;width:1200px;height:621px;background:var(--grey-bg)}
.quotes-title{left:0;top:2480px;width:1200px;text-align:center;font-size:26px;color:var(--blue)}
.qmark{left:246px;width:44px;height:36px}
.quote{left:297px;width:630px;font-style:italic;font-weight:300;font-size:16.5px;line-height:26px;color:#333}
.author{left:770px;font-family:"Montserrat",sans-serif;font-weight:700;font-size:17px;color:var(--ink)}
.author-role{left:770px;font-size:11px;color:#555}
/* footer */
.footer{left:0;top:3033px;width:1200px;height:689px;background:var(--navy)}
.footer-logo{left:289px;top:3146px;font-size:22px;color:var(--white)}
.contact-icon{left:289px;width:46px;height:40px}
.contact-text{left:348px;font-size:14.5px;line-height:25px;color:var(--white)}
.form-title{left:614px;top:3124px;font-size:26px;color:var(--blue)}
.label{left:614px;font-family:"Montserrat",sans-serif;font-weight:700;font-size:10px;color:var(--white)}
.field{left:614px;width:297px;height:31px;background:var(--white);font-size:11px;color:#bbb;padding:8px 10px}
.send-btn{left:614px;top:3512px;width:297px;height:38px;background:var(--btn-blue)}
.legal{right:289px;top:3588px;font-size:14px;color:var(--white)}
.legal span{text-decoration:underline}
</style>
</head>
<body>

<header>
  <div class="abs brand site-logo"><span class="dot"></span>WOHNWERK FRANKEN</div>
  <nav class="abs main-nav"><span>Mieter/Käufer</span><span>Vermieter/verkäufer</span><span>Bauträger</span><span>Service</span><span>Über uns</span></nav>
</header>

<h1 class="abs heading hero-title">Ihr Immobilienmakler für<br>die Metropolregion Nürnberg</h1>

<div class="abs tile" style="left:126px;background:linear-gradient(135deg,#8a5a7e,#b58a98 55%,#6b4a68)" role="img" aria-label="Foto: junge Familie mit Baby"></div>
<div class="abs tile" style="left:450px;background:linear-gradient(180deg,#7a86a6,#4f5877 55%,#9a8c80)" role="img" aria-label="Foto: beleuchtetes Einfamilienhaus am Abend"></div>
<div class="abs tile" style="left:775px;background:linear-gradient(160deg,#2f7fc8,#4a9ad8 55%,#8a7a5a)" role="img" aria-label="Foto: Baukräne über einem Rohbau"></div>
<div class="abs tile-caption" style="left:126px">→ Für Mieter/Käufer</div>
<div class="abs tile-caption" style="left:450px">→ Für Vermieter/Verkäufer</div>
<div class="abs tile-caption" style="left:775px">→ Für Bauträger</div>

<h2 class="abs heading intro-title">Die richtige Wahl des Immobilienmaklers</h2>
<div class="abs intro-text">
  <p>Herzlich Willkommen bei der Lukas Brennholt Immobilienberatung in Nürnberg! Sie suchen den passenden Partner rund um das umfassende Thema Immobilien? Dann sind Sie hier genau richtig: egal ob Suche, Verkauf oder Vermietung einer Eigentumswohnung oder eines Hauses. Bei einem so komplexen Thema mit hohen Emotionen, Sachwerten und Auswirkungen auf Ihr tägliches Leben geht es um Vertrauen und ein gutes Gefühl. Sie sollen eine überzeugende Dienstleistung von Ihrem Makler erhalten.<br>Eine umfassende und professionelle Beratung ist dabei für Ihre Zufriedenheit entscheidend. Davon können Sie sich als Eigentümer schon beim ersten gemeinsamen Schritt überzeugen: der transparenten Einwertung Ihrer Immobilie.</p>
  <p>Vertrauen Sie bei der Wahl des Maklers auf die Kombination aus Ausbildung, Erfahrung und Engagement. Als ausgebildeter Immobilienkaufmann (IHK) war bzw. bin ich als selbstständiger Kooperationspartner für namhafte Bauträger wie die Kellermann Wohnbau AG, die R&amp;T Gruppe GmbH oder die Seidl Bau GmbH &amp; Co. KG tätig. Daraus resultiert eine sehr gute Kenntnis des regionalen Immobilienmarktes in Nürnberg, Fürth, Erlangen, Schwabach und der weiteren Umgebung. Sie werden den Unterschied merken!</p>
</div>
<div class="abs cta-label">Sie sind Eigentümer einer Immobilie?</div>
<div class="abs btn cta-btn">→ Jetzt bewerten lassen</div>

<section>
  <div class="abs band" role="img" aria-label="Abgedunkeltes Foto: Altstadt von Nürnberg unter Wolkenhimmel"></div>
  <div class="abs band-kicker">Das können wir für Sie tun</div>
  <h2 class="abs heading band-title">Wenn Sie eine Immobilie verkaufen oder vermieten möchten</h2>
  <div class="abs band-link">→ Alle Leistungen</div>

  <svg class="abs service-icon" style="left:124px" viewBox="0 0 72 72" fill="none" stroke="#fff" stroke-width="2.5"><path d="M4 34 36 8l32 26"/><path d="M12 28v38h48V28"/><rect x="18" y="36" width="12" height="12"/><path d="M24 36v12M18 42h12"/><rect x="38" y="44" width="12" height="22"/><path d="M2 66h68"/></svg>
  <div class="abs service" style="left:225px"><h3>Objektaufnahme</h3><p>Die ersten Schritte sind die detaillierte Einwertung, Preisfindung, Vermessung und Fotografie Ihrer Immobilie. Daraus entsteht das Exposé u.a. mit hochwertigen Bildern und einer ausführlichen Beschreibung.</p></div>

  <svg class="abs service-icon" style="left:450px" viewBox="0 0 72 72" fill="none" stroke="#fff" stroke-width="2.5"><rect x="4" y="6" width="50" height="62" rx="2"/><path d="M16 16h30M16 26h30M16 36h14"/><circle cx="11" cy="16" r="2"/><circle cx="11" cy="26" r="2"/><circle cx="22" cy="54" r="9"/><path d="M22 45v9h9"/><path d="M62 8v52l-3 8-3-8V8z"/></svg>
  <div class="abs service" style="left:543px"><h3>Vermarktung</h3><p>Gemeinsam legen wir ein Konzept fest, wie Ihre Immobilie am besten präsentiert wird. Dazu erhalten Sie einen ausführlichen Vorschlag mit vielen Auswahlmöglichkeiten, den wir an Ihre Wünsche und Vorstellungen anpassen.</p></div>

  <svg class="abs service-icon" style="left:775px" viewBox="0 0 72 72" fill="none" stroke="#fff" stroke-width="2.5"><path d="M36 4v64M2 68h36M36 10H6v26h30"/><rect x="10" y="15" width="22" height="14"/></svg>
  <div class="abs service" style="left:869px"><h3>Vertragsabschluss</h3><p>Danach folgt die Vorbereitung und Unterzeichnung des Vertrages. Dabei werden die Interessen aller Parteien berücksichtigt und ausführlich besprochen. Alle Parteien sollen mit dem Abschluss vollkommen zufrieden sein.</p></div>
</section>

<section>
  <h2 class="abs heading ref-title">Erfolgreich vermittelte Objekte</h2>
  <p class="abs ref-text">Lorem ipsum dolor sit amet, consetetur sadipscing elitr, sed diam nonumy eirmod tempor invidunt ut labore et dolore magna aliquyam erat, sed diam voluptua.</p>
  <article class="abs card" style="left:126px;background:linear-gradient(180deg,#5f86c9 0%,#a9b7cc 35%,#6c7380 75%,#3a3f3a 100%)" role="img" aria-label="Foto: moderne Mehrfamilienhäuser">
    <div class="card-frame"></div><h4>Exklusiv und ruhig</h4><div class="sub">Lorem ipsum dolor sit amet</div><div class="btn">→ Objekt ansehen</div>
  </article>
  <article class="abs card" style="left:614px;background:linear-gradient(180deg,#6f93cf 0%,#c8cfd8 35%,#8e9196 75%,#3e423e 100%)" role="img" aria-label="Foto: weißes Einfamilienhaus mit Satteldach">
    <div class="card-frame"></div><h4>Moderner Luxus</h4><div class="sub">Lorem ipsum dolor sit amet</div><div class="btn">→ Objekt ansehen</div>
  </article>
</section>

<section>
  <div class="abs quotes-bg"></div>
  <h2 class="abs heading quotes-title">Das sagen unsere Kunden über uns</h2>
  <svg class="abs qmark" style="top:2562px" viewBox="0 0 44 36" fill="#8a8d96"><path d="M4 36l6-18H4V0h16v18L14 36zM26 36l6-18h-6V0h16v18l-6 18z"/></svg>
  <p class="abs quote" style="top:2562px">Äußerst kundenorientiertes und freundliches Auftreten. Sehr große Fachkompetenz sowie überaus seriöse Abwicklung bei Kauf bzw. Verkauf als auch bei Vermietung von Objekten. Kann man wirklich zu 100% weiterempfehlen!</p>
  <div class="abs author" style="top:2651px">Sabine und Jörg M.</div>
  <div class="abs author-role" style="top:2675px">(Käufer und Vermieter)</div>
  <svg class="abs qmark" style="top:2786px" viewBox="0 0 44 36" fill="#8a8d96"><path d="M4 36l6-18H4V0h16v18L14 36zM26 36l6-18h-6V0h16v18l-6 18z"/></svg>
  <p class="abs quote" style="top:2786px">Ich würde Herrn Brennholt als freundlich, zuverlässig und integer beschreiben. Eigenschaften, die in dieser Kombination nicht branchentypisch sind. Er hat uns beim Erwerb einer Eigentumswohnung sehr kompetent beraten und bis zum Abschluss herausragend begleitet. Ich kann die "Lukas Brennholt Immobilienberatung" wirklich uneingeschränkt empfehlen.</p>
  <div class="abs author" style="top:2927px">Peter L.</div>
  <div class="abs author-role" style="top:2951px">(Käufer)</div>
</section>

<footer>
  <div class="abs footer"></div>
  <div class="abs brand footer-logo"><span class="dot"></span>WOHNWERK FRANKEN</div>

  <svg class="abs contact-icon" style="top:3275px" viewBox="0 0 46 40" fill="#fff"><path d="M23 2 1 21h6v17h12V27h8v11h12V21h6z"/></svg>
  <div class="abs contact-text" style="top:3270px">Lindenhofstraße 12<br>90480 Nürnberg</div>
  <svg class="abs contact-icon" style="top:3353px" viewBox="0 0 46 40" fill="#fff"><path d="M4 12c0-6 38-6 38 0v4h-9v-4c-6-2-14-2-20 0v4H4z"/><path d="M10 18h26l4 18H6z"/><circle cx="23" cy="27" r="5" fill="#1b2340"/></svg>
  <div class="abs contact-text" style="top:3358px">0911 5550 1234</div>
  <svg class="abs contact-icon" style="top:3416px" viewBox="0 0 46 40" fill="none" stroke="#fff" stroke-width="3"><rect x="15" y="2" width="16" height="36" rx="3"/><path d="M20 32h6"/></svg>
  <div class="abs contact-text" style="top:3422px">0176 5550 9876</div>
  <svg class="abs contact-icon" style="top:3482px" viewBox="0 0 46 40" fill="#fff"><path d="M42 2 2 20l12 5 3 13 6-9 10 7z"/></svg>
  <div class="abs contact-text" style="top:3485px">lb@wohnwerk-franken.de</div>

  <h2 class="abs heading form-title">Wir sind gerne für Sie da:</h2>
  <div class="abs label" style="top:3192px">Vollständiger Name</div>
  <div class="abs field" style="top:3209px">z.B. Max Mustermann</div>
  <div class="abs label" style="top:3261px">E-Mail</div>
  <div class="abs field" style="top:3278px">z.B. mustermann@email.de</div>
  <div class="abs label" style="top:3330px">Telefon</div>
  <div class="abs field" style="top:3347px">Wie erreichen wir Sie am besten?</div>
  <div class="abs label" style="top:3399px">Was möchten Sie uns mitteilen?</div>
  <div class="abs field" style="top:3415px;height:82px">Ihre Nachricht</div>
  <div class="abs btn send-btn">→ Nachricht absenden</div>
  <div class="abs legal"><span>Datenschutz</span> | <span>Impressum</span></div>
</footer>

</body>
</html>
```